Packaging design for Velmurin / Packaging design for Velmurin

Hello everybody, we're the Velmurin team, we're a family business working in the food industry. From father to son, Velmurin's been passionated about the culture of olives. What we need: a design to impress a bag of green olives in a spicy red sauce and a bag of black olives in a black sauce. What we're looking for: a european / mediterranean style with a warm vibe. The product's target: the North American market. The print of the design will be done on a 18cm x 18cm, 7.1in x 7.1in transparent plastic bag. Therefore, we will see the olives in their sauce in the bag. The design for the bag of green olives must contain: - The ingredients in three languages ​​(french-english-arabic): olives, spices, chilli pepper, vegetable oil, garlic. - bright shiny colors; - the net weight of 450 g; - an oval stamp that says '' Product of Algeria - Flavor unique - Product of Algeria ''; - the name of the brand: '' Velmurin ''; - another stamp that says "sigois olives" - the name of the product, "broken olives spicy / spicy broken olives", in both English and French. The design for the bag of black olives must contain: - The ingredients in english-french-arabic: black olives, salt. - a black background; - the net weight of 450 g; - an oval stamp that says '' Product of Algeria - Flavor unique - Product of Algeria ''; - the name of the brand: '' Velmurin ''; - another stamp that says '' Olives sigoises ''; - the name of the product, '' Black Olives in Greek Style / Black Olives Greek Style '', in both French and English; - the '' caliber 19/21 '' indication. Mostly, we do not want a standard design reproducing the image of the product, we want it to cloak the whole package. Do not hesitate to think outside the box. *** We need a design for an impression of a bag of olives. We need it for green olives in a spicy sauce with red peppers, and also for black olives. We are looking for a European / Mediterranean style with a warm atmosphere. The product is intended for North America. The printing will be done on a transparent plastic bag of 18cmx18cm, 7.1in x 7.1in, the green olives in their red sauce and the black olives in their black sauce will be very apparent. An example of design is attached in the photos (Lumo Kar bag). The bag for green olives would include: - ingredients in three languages ​​(French - English - Arabic): olives, spices, peppers, vegetable oil, garlic. - bright colors, - the net weight of 450 g, - an oval seal indicating "Product of Algeria - Flavor unique - Product of Algeria", - the mark "Velmurin", - another stamp indicating "sigillian olives", - the name of the product in English and French "Spicy Broken Olives / Spicy Broken Olives". The bag for black olives would include: - ingredients in three languages ​​(French, English, Arabic): Black olives, salt. - a black background, - the net weight of 450 g, - an oval stamp stating "Product of Algeria - Flavor unique - Product of Algeria", - another stamp indicating "Olives sigoises", - the name of the product in French and in English "Black olives Greek style / Black olives greek style", - the indication "caliber 19/21". We do not want a standard label simply reproducing images of olives, but rather a package with a transparent design. We want something out of the box. Thanks and good luck. Thanks guys and good luck.

Target Market(s)

North America / North America

Industry/Entity Type

Food Production

Font styles to use
Serif
Sans Serif
Script

Colors

Designer to choose colors to be used in the design.

Requirements
Must have
• -Velmurin - barcode / barcode - nutrition facts / nutrition facts - net weight / net weight - the recyclable sign / the recycable sign - to consume before / to be consumed before
Nice to have
• - the stamp "Olives sigoises" / the stamp "Olives sigoises" - the vintage drawing of an olive tree / a vintage drawing of an olive tree - an oval stamp indicating "Product of Algeria - Flavor unique - Product of Algeria" / An Oval Stamp That Says '' Product of Algeria - Flavor Unique - Product of Algeria '' - ALL the bag should be covered by the design while letting the olives show / ALL the bag should be covered by the design but still let the olives be apparent
Should not have
• no label (the print will be on the bag) / no label (the print will be done directly on the bag)

```html
<!DOCTYPE html>
<html lang="en">
<head>
<meta charset="utf-8">
<title>Velmurin Green Olives – Bag Print</title>
<link href="https://fonts.googleapis.com/css2?family=Uncial+Antiqua&family=Open+Sans:wght@600;700&display=swap" rel="stylesheet">
<style>
  :root {
    --page-bg: #f3f3ee;
    --sage-light: #dfe8c4;
    --olive-dark: #5a6424;
    --olive-mid: #6b7f38;
    --shield-green: #5d7a2c;
    --gold: #c9a45a;
    --ink-dark: #4f5522;
    --ink-light: #eef1db;
    --cream: #f4f1dc;
    --seal-red: #8e1f22;
  }
  * { margin: 0; padding: 0; box-sizing: border-box; }
  html, body { width: 1200px; height: 1200px; overflow: hidden; background: var(--page-bg); }
  .bag-print {
    position: absolute; left: 80px; top: 80px; width: 1040px; height: 1040px;
    font-family: "Open Sans", Arial, sans-serif;
  }
  .bag-print svg.artwork { position: absolute; inset: 0; }
  .brand-name {
    position: absolute; left: 293px; width: 447px; top: 104px; height: 70px;
    display: flex; align-items: center; justify-content: center;
    font-family: "Uncial Antiqua", serif; font-size: 50px; color: var(--olive-dark);
    letter-spacing: 1px;
  }
  .ingredients { position: absolute; font-weight: 600; font-size: 19px; line-height: 27px; }
  .ingredients h3 { font-size: 19px; font-weight: 700; text-align: center; margin-bottom: 2px; }
  .ingredients p { text-align: justify; text-align-last: center; }
  .ingredients--left { left: 37px; top: 293px; width: 224px; color: var(--ink-dark); }
  .ingredients--right { left: 771px; top: 293px; width: 224px; color: var(--ink-light); }
  .ingredients--bottom { left: 180px; top: 848px; width: 680px; color: var(--ink-light); }
  .product-title {
    position: absolute; left: 293px; width: 447px; text-align: center;
    font-family: "Uncial Antiqua", serif; color: var(--ink-dark);
  }
  .product-title--main { top: 483px; font-size: 76px; line-height: 90px; }
  .product-title--fr { top: 578px; font-size: 24px; }
  .product-title--en { top: 610px; font-size: 24px; }
  .variety-ribbon-text {
    position: absolute; left: 293px; width: 447px; top: 700px; text-align: center;
    font-family: "Uncial Antiqua", serif; font-size: 44px; color: var(--cream);
  }
  .net-weight {
    position: absolute; left: 0; width: 1040px; top: 988px; text-align: center;
    font-weight: 600; font-size: 19px; color: var(--ink-light);
  }
</style>
</head>
<body>
<main class="bag-print">
  <svg class="artwork" width="1040" height="1040" viewBox="0 0 1040 1040">
    <defs>
      <linearGradient id="shieldInner" x1="0" y1="0" x2="0" y2="1">
        <stop offset="0" stop-color="#f4f6e6"/>
        <stop offset="0.7" stop-color="#e9edd4"/>
        <stop offset="1" stop-color="#c9d2a6"/>
      </linearGradient>
      <linearGradient id="branchArea" x1="0" y1="0" x2="1" y2="1">
        <stop offset="0" stop-color="#9fb25e"/>
        <stop offset="1" stop-color="#6f8a34"/>
      </linearGradient>
    </defs>
    <!-- background split -->
    <rect class="panel-light" width="1040" height="1040" fill="var(--sage-light)"/>
    <polygon class="panel-dark" points="1040,0 1040,1040 0,1040" fill="var(--olive-dark)"/>

    <!-- brand banner -->
    <g class="brand-banner">
      <line x1="300" y1="139" x2="340" y2="139" stroke="var(--gold)" stroke-width="4"/>
      <line x1="693" y1="139" x2="733" y2="139" stroke="var(--gold)" stroke-width="4"/>
      <rect x="300" y="116" width="42" height="46" rx="10" fill="var(--olive-mid)" stroke="var(--gold)" stroke-width="3"/>
      <rect x="691" y="116" width="42" height="46" rx="10" fill="var(--olive-mid)" stroke="var(--gold)" stroke-width="3"/>
      <rect x="340" y="92" width="353" height="96" fill="var(--sage-light)" stroke="var(--olive-mid)" stroke-width="4"/>
      <rect x="350" y="102" width="333" height="76" fill="none" stroke="var(--gold)" stroke-width="2"/>
    </g>

    <!-- shield crest -->
    <g class="crest">
      <path d="M300 280 Q520 225 740 280 L740 520 Q740 705 520 805 Q300 705 300 520 Z" fill="var(--gold)"/>
      <path d="M308 286 Q520 235 732 286 L732 520 Q732 698 520 795 Q308 698 308 520 Z" fill="var(--shield-green)"/>
      <path d="M330 302 Q520 258 710 302 L710 520 Q710 680 520 770 Q330 680 330 520 Z" fill="url(#shieldInner)" stroke="var(--gold)" stroke-width="2"/>
      <path role="img" aria-label="Illustration of a green olive branch with olives and leaves"
            d="M350 318 Q520 280 690 318 L690 470 Q520 500 350 470 Z" fill="url(#branchArea)" opacity="0.85"/>
    </g>

    <!-- variety ribbon -->
    <g class="variety-ribbon">
      <polygon points="280,700 320,690 320,770 280,778 298,740" fill="#4e6326"/>
      <polygon points="760,700 720,690 720,770 760,778 742,740" fill="#4e6326"/>
      <path d="M310 688 Q520 670 730 688 L730 768 Q520 750 310 768 Z" fill="var(--olive-mid)" stroke="var(--gold)" stroke-width="2"/>
    </g>

    <!-- stamps -->
    <g class="stamps">
      <circle cx="83" cy="747" r="47" fill="#f0f2e2" stroke="var(--olive-mid)" stroke-width="4"/>
      <circle cx="83" cy="747" r="36" fill="none" stroke="var(--olive-mid)" stroke-width="2"/>
      <circle cx="87" cy="853" r="40" fill="var(--seal-red)"/>
      <circle cx="957" cy="747" r="47" fill="#f0f2e2" stroke="var(--olive-mid)" stroke-width="4"/>
      <circle cx="957" cy="747" r="36" fill="none" stroke="var(--olive-mid)" stroke-width="2"/>
      <circle cx="963" cy="853" r="40" fill="var(--seal-red)"/>
    </g>
  </svg>

  <div class="brand-name">Velmurin</div>

  <section class="ingredients ingredients--left">
    <h3>Ingredients:</h3>
    <p>Lorem ipsum dolor sit amet, consectetuer adipiscing elit, sed diam nonummy nibh euismod tincidunt ut laoreet dolore magna aliquam erat volutpat. Ut wisi enim ad minim veniam, quis nostrud exerci tation ullamcorper suscipit</p>
  </section>

  <section class="ingredients ingredients--right">
    <h3>Ingredients:</h3>
    <p>Lorem ipsum dolor sit amet, consectetuer adipiscing elit, sed diam nonummy nibh euismod tincidunt ut laoreet dolore magna aliquam erat volutpat. Ut wisi enim ad minim veniam, quis nostrud exerci tation ullamcorper suscipit</p>
  </section>

  <h1 class="product-title product-title--main">Olives</h1>
  <p class="product-title product-title--fr">Cassées épicées</p>
  <p class="product-title product-title--en">Spicy broken olives</p>
  <p class="variety-ribbon-text">Green Olives</p>

  <section class="ingredients ingredients--bottom">
    <h3>Ingredients:</h3>
    <p>Lorem ipsum dolor sit amet, consectetuer adipiscing elit, sed diam nonummy nibh euismod tincidunt ut laoreet dolore magna aliquam erat volutpat. Ut wisi enim ad minim veniam, quis nostrud exerci tation ullamcorper suscipit</p>
  </section>

  <p class="net-weight">NET WT 450 g</p>
</main>
</body>
</html>
```